Need Web Banners Designed for Mobile Banking App

We need a web banner designed to introduce the launch of our Mobile Banking App.

About our App:
Members can enjoy fast, easy and secure access to their accounts on the go. It’s the convenient way to manage your accounts, transfer funds, pay bills and more… no matter where you are!

Requirements:
We need 2 sizes of the Banner (no more than 300 dpi). Banners are to be the same design, we just need 2 different sizes.

Banner 1. 754px (width) x 209px (height)
Banner 2. 8 inches (wide) x 1.5 inches (height)

Colors to use: We like blues and find it goes well on our website but we don't have any color requirements.

Banner should contain the following:

- Headline Text:
We've always been local, now we're mobile.

- Sub-headline Text:
Introducing the HMF Mobile App for Tovix and Merovel.

- "Available on the kit market" badge". See attached for example. Should not include the Brindle logo since our app is available for both Tovix and Merovel.

Attached is also a screen shot of the Mobile Banking App that the member will see when they log into their account. This can be used if it fits in with your design but it's optional.

```html
<!DOCTYPE html>
<html lang="en">
<head>
<meta charset="utf-8">
<title>HMF Mobile App Banner</title>
<link rel="stylesheet" href="https://fonts.googleapis.com/css2?family=Arimo:ital,wght@0,400;0,700;1,700&display=swap">
<style>
  :root {
    --ink: #111111;
    --brand-blue: #1b7fc0;
    --button-top: #35b3ea;
    --button-bottom: #0f79b8;
    --bg-light: #e4e3df;
    --bg-mid: #d2d0cb;
    --photo-warm: #b9ad9c;
    --photo-cool: #8e9396;
    --badge: #000000;
    --white: #ffffff;
  }
  html, body {
    margin: 0;
    padding: 0;
    overflow: hidden;
  }
  .banner {
    position: relative;
    width: 1200px;
    height: 333px;
    overflow: hidden;
    font-family: "Arimo", Arial, sans-serif;
    background: linear-gradient(90deg, var(--bg-mid) 0%, var(--bg-light) 45%, var(--bg-light) 100%);
  }
  .hero-photo {
    position: absolute;
    left: 0;
    top: 0;
    width: 560px;
    height: 333px;
    background:
      radial-gradient(ellipse 160px 260px at 230px 170px, var(--photo-cool) 0%, rgba(142,147,150,0) 100%),
      linear-gradient(90deg, var(--photo-warm) 0%, rgba(185,173,156,0.6) 55%, rgba(228,227,223,0) 100%);
  }
  .headline {
    position: absolute;
    right: 20px;
    top: 34px;
    margin: 0;
    text-align: right;
    font-weight: 700;
    text-transform: uppercase;
    line-height: 1;
  }
  .headline-local {
    display: block;
    font-size: 49px;
    color: var(--ink);
    letter-spacing: 0.5px;
  }
  .headline-mobile {
    display: block;
    margin-top: 12px;
    font-size: 49px;
    color: var(--brand-blue);
    letter-spacing: 0.5px;
  }
  .subheadline {
    position: absolute;
    right: 20px;
    top: 146px;
    margin: 0;
    font-size: 19px;
    color: var(--ink);
  }
  .cta-button {
    position: absolute;
    left: 796px;
    top: 224px;
    width: 300px;
    height: 64px;
    border-radius: 8px;
    background: linear-gradient(180deg, var(--button-top) 0%, var(--button-bottom) 100%);
    box-shadow: 0 4px 8px rgba(0,0,0,0.3);
    display: flex;
    align-items: center;
    justify-content: center;
    gap: 18px;
    color: var(--white);
    font-size: 31px;
    font-weight: 700;
    font-style: italic;
    text-decoration: none;
  }
  .cta-icon {
    width: 20px;
    height: 24px;
  }
  .store-badge {
    position: absolute;
    left: 16px;
    top: 266px;
    width: 121px;
    height: 47px;
    border-radius: 7px;
    background: var(--badge);
    border: 1px solid #8a8a8a;
    box-sizing: border-box;
  }
</style>
</head>
<body>
  <div class="banner">
    <div class="hero-photo" role="img" aria-label="Photo of a person in a checked shirt holding a smartphone, over a faded mobile banking app screen"></div>

    <h1 class="headline">
      <span class="headline-local">We've Always Been Local</span>
      <span class="headline-mobile">Now We're Mobile</span>
    </h1>
    <p class="subheadline">Introducing the HMF Mobile App for Tovix and Merovel</p>

    <a class="cta-button" href="#">
      <svg class="cta-icon" viewBox="0 0 20 24" aria-hidden="true">
        <polygon points="0,0 20,12 0,24" fill="#ffffff"/>
      </svg>
      <span>Get it NOW!</span>
    </a>

    <div class="store-badge" role="img" aria-label="Kit market listing badge"></div>
  </div>
</body>
</html>
```